KRV e-payment Business Card Design

We require a new business card design to suit our expanding consulting business -who are specialists in 2 main areas
1. Advising large Corporations and Government organisation on how to improve the why they use emerging (B2B) electronic payment systems
2. Educate Global and regional banks on how to design, build and market electronic business payment products in emerging markets

Our logo is grey/silver based with a building block theme. It also suggests "insight" and business know-how capitalizing on our KRV name. We also want to engender trust,security and balance via the ying/yan symbol

The design needs to take into account the target regional areas of Australiasia/Asia Pacific/Middle East and Africa

Target Market(s)

Regional Banks and their business customers

Industry/Entity Type

Electronic

Contact Information for Business Card

Marcus Dellwyn
Director KRV Consulting (Aust) Pty Ltd
PO Box 4736
Brambleton NSW 2164
Australia
tel +61 (0) 2 95316407
mob +61 (0) 438275601
krvconsulting@lumenpost.com

```html
<!DOCTYPE html>
<html lang="en">
<head>
<meta charset="utf-8">
<title>KRV e-payment Business Cards</title>
<link rel="stylesheet" href="https://fonts.googleapis.com/css2?family=EB+Garamond:ital,wght@0,500;0,600;1,500&display=swap">
<style>
  :root {
    --ink: #111111;
    --paper: #ffffff;
    --band: #151515;
    --charcoal: #3b3b3b;
    --mid-grey: #a6a6a6;
    --soft-grey: #c9c9c9;
    --pale-grey: #e3e3e3;
  }
  html, body {
    margin: 0;
    padding: 0;
    width: 1200px;
    height: 2346px;
    overflow: hidden;
    background: var(--paper);
    font-family: "EB Garamond", "Times New Roman", serif;
  }
  .card {
    position: relative;
    width: 1200px;
    height: 782px;
    overflow: hidden;
  }
  .card__top { position: absolute; left: 0; top: 0; width: 1200px; height: 340px; }
  .card__band { position: absolute; left: 0; top: 40px; width: 1200px; height: 120px; background: var(--band); }
  .card__subband { position: absolute; left: 380px; top: 160px; width: 820px; height: 90px; }
  .brand {
    position: absolute; left: 30px; top: 20px;
    width: 300px; height: 260px;
    background: var(--paper);
    border: 3px solid var(--ink);
    box-sizing: border-box;
    display: flex; align-items: center; justify-content: center;
  }
  .brand__name {
    font-size: 120px; font-weight: 500; color: var(--ink);
    letter-spacing: 6px; line-height: 1;
  }
  .brand__division {
    position: absolute; left: 425px; top: 78px;
    padding: 6px 16px;
    background: var(--paper);
    border: 3px solid var(--ink);
    font-size: 32px; font-style: italic; font-weight: 500; color: var(--ink);
    white-space: nowrap;
  }
  .brand__tagline {
    position: absolute; left: 80px; top: 296px;
    font-size: 22px; font-style: italic; font-weight: 500; color: var(--ink);
  }
  .contact {
    position: absolute; left: 0; top: 380px; width: 1200px;
    font-size: 40px; font-weight: 600; line-height: 60px;
  }
  .contact__line { position: relative; height: 60px; text-align: center; white-space: nowrap; }
  .contact__country { position: absolute; left: 385px; }
  .contact__phone { position: absolute; left: 600px; }

  .card--charcoal { background: var(--charcoal); }
  .card--charcoal .card__top { background: var(--paper); }
  .card--charcoal .card__subband { background: var(--soft-grey); }
  .card--charcoal .contact { color: var(--paper); }

  .card--grey { background: var(--mid-grey); }
  .card--grey .card__top { background: var(--mid-grey); }
  .card--grey .card__subband { background: var(--soft-grey); }
  .card--grey .contact { color: var(--ink); }

  .card--pale { background: var(--pale-grey); }
  .card--pale .card__top { background: var(--pale-grey); }
  .card--pale .card__subband { background: var(--pale-grey); }
  .card--pale .contact { color: var(--ink); }
</style>
</head>
<body>

<section class="card card--charcoal">
  <div class="card__top"></div>
  <div class="card__band"></div>
  <div class="card__subband"></div>
  <div class="brand"><span class="brand__name">KRV</span></div>
  <div class="brand__division">Consulting (Australia) Pty Ltd</div>
  <div class="brand__tagline">"real e-payment insight"</div>
  <div class="contact">
    <div class="contact__line">Marcus Dellwyn Director KRV Consulting (Aust) Pty Ltd</div>
    <div class="contact__line">PO Box 4736 Brambleton NSW 2164</div>
    <div class="contact__line"><span class="contact__country">Australia</span><span class="contact__phone">Tel +61 (0) 2 95316407</span></div>
    <div class="contact__line"><span class="contact__phone">Mob +61 (0) 438275601</span></div>
    <div class="contact__line">E-mail: krvconsulting@lumenpost.com</div>
  </div>
</section>

<section class="card card--grey">
  <div class="card__top"></div>
  <div class="card__band"></div>
  <div class="card__subband"></div>
  <div class="brand"><span class="brand__name">KRV</span></div>
  <div class="brand__division">Consulting (Australia) Pty Ltd</div>
  <div class="brand__tagline">"real e-payment insight"</div>
  <div class="contact">
    <div class="contact__line">Marcus Dellwyn Director KRV Consulting (Aust) Pty Ltd</div>
    <div class="contact__line">PO Box 4736 Brambleton NSW 2164</div>
    <div class="contact__line"><span class="contact__country">Australia</span><span class="contact__phone">Tel +61 (0) 2 95316407</span></div>
    <div class="contact__line"><span class="contact__phone">Mob +61 (0) 438275601</span></div>
    <div class="contact__line">E-mail: krvconsulting@lumenpost.com</div>
  </div>
</section>

<section class="card card--pale">
  <div class="card__top"></div>
  <div class="card__band"></div>
  <div class="card__subband"></div>
  <div class="brand"><span class="brand__name">KRV</span></div>
  <div class="brand__division">Consulting (Australia) Pty Ltd</div>
  <div class="brand__tagline">"real e-payment insight"</div>
  <div class="contact">
    <div class="contact__line">Marcus Dellwyn Director KRV Consulting (Aust) Pty Ltd</div>
    <div class="contact__line">PO Box 4736 Brambleton NSW 2164</div>
    <div class="contact__line"><span class="contact__country">Australia</span><span class="contact__phone">Tel +61 (0) 2 95316407</span></div>
    <div class="contact__line"><span class="contact__phone">Mob +61 (0) 438275601</span></div>
    <div class="contact__line">E-mail: krvconsulting@lumenpost.com</div>
  </div>
</section>

</body>
</html>
```